Brindlow Engineering Business Card

our company has just rebranded and taken on a new logo design. We now need to update our business cards with the new logo. This is also an opportunity to reformat and modernize our look. We are an engineering company so the look needs to be formal and professional yet it should look modern. Have a look at our current card and the new card should have the same information.

Target Market(s)

Engineering firms, government, mining companies

Industry/Entity Type

Mechanical Engineering

Contact Information for Business Card

Requirements
Must have
• look professional and modern
Should not have
• should not include the office locations 'Brisbane, Sydney and Kuala Lumpur'
• you will find this on the example but it should not be included in these versions. please remove from your submissions and resubmit

```html
<!DOCTYPE html>
<html lang="en">
<head>
<meta charset="utf-8">
<title>Brindlow Engineering – Business Card</title>
<link href="https://fonts.googleapis.com/css2?family=Saira:wght@400;500;600&display=swap" rel="stylesheet">
<style>
  :root{
    --stage:#dcdcdc;
    --card:#eef0f2;
    --brand:#3a4fa8;
    --band-deep:#2a4ec4;
    --band-mid:#1f8fe0;
    --band-light:#27a6ea;
    --silver-hi:#f4f5f7;
    --silver-lo:#8c9096;
    --white:#ffffff;
    --ink:#4a4d55;
  }
  html,body{margin:0;padding:0;overflow:hidden;}
  body{width:1200px;height:769px;background:var(--stage);position:relative;font-family:"Saira",sans-serif;}
  .card{position:absolute;left:150px;top:125px;width:900px;height:520px;background:var(--card);border-radius:22px;overflow:hidden;box-shadow:0 10px 30px rgba(0,0,0,.15);}
  .brand{position:absolute;left:190px;top:70px;display:flex;align-items:center;gap:22px;}
  .brand-dot{width:76px;height:76px;border-radius:50%;background:var(--brand);}
  .brand-name{color:var(--brand);font-weight:600;line-height:1;text-transform:uppercase;}
  .brand-name .line1{display:block;font-size:58px;letter-spacing:1px;}
  .brand-name .line2{display:block;font-size:27px;letter-spacing:7px;margin-top:6px;}
  .band{position:absolute;left:0;top:240px;width:900px;height:227px;
    background:radial-gradient(ellipse at 60% 50%,var(--band-light) 0%,var(--band-mid) 40%,var(--band-deep) 100%);}
  .rule{position:absolute;left:0;width:900px;height:7px;background:linear-gradient(90deg,var(--silver-lo),var(--silver-hi) 30%,var(--silver-lo) 60%,var(--silver-hi) 85%,var(--silver-lo));}
  .rule.top{top:233px;}
  .rule.bottom{top:467px;}
  .notch{position:absolute;left:193px;top:240px;}
  .person{position:absolute;left:68px;top:305px;width:300px;text-align:center;color:var(--white);}
  .person-name{font-size:27px;font-weight:500;letter-spacing:1px;text-transform:uppercase;line-height:1.1;}
  .person-role{font-size:20px;line-height:1.3;}
  .divider{position:absolute;left:427px;top:282px;width:2px;height:160px;background:rgba(255,255,255,.8);}
  .contacts{position:absolute;left:472px;top:294px;margin:0;padding:0;list-style:none;color:var(--white);font-size:17px;letter-spacing:.5px;}
  .contacts li{display:flex;align-items:center;gap:10px;height:33px;}
  .contacts svg{width:20px;height:20px;flex:none;}
  .website{position:absolute;left:0;top:480px;width:900px;text-align:center;color:var(--ink);font-size:20px;letter-spacing:2px;font-weight:500;}
</style>
</head>
<body>
  <div class="card">
    <div class="brand">
      <div class="brand-dot"></div>
      <div class="brand-name"><span class="line1">Brindlow</span><span class="line2">Engineering</span></div>
    </div>

    <div class="rule top"></div>
    <div class="band"></div>
    <svg class="notch" width="26" height="18" viewBox="0 0 26 18"><polygon points="0,0 26,0 13,18" fill="var(--card)"/></svg>
    <div class="rule bottom"></div>

    <div class="person">
      <div class="person-name">Daniel Marsh</div>
      <div class="person-role">Managing Director</div>
    </div>

    <div class="divider"></div>

    <ul class="contacts">
      <li>
        <svg viewBox="0 0 20 20"><circle cx="10" cy="10" r="10" fill="#fff"/><path d="M7 5.5l1.6 2.4-1 1c.6 1.3 1.5 2.2 2.8 2.8l1-1 2.4 1.6-1 1.7c-3.4-.4-6.3-3.3-6.7-6.7z" fill="var(--band-deep)"/></svg>
        <span>021 555 0147</span>
      </li>
      <li>
        <svg viewBox="0 0 20 20"><circle cx="10" cy="10" r="10" fill="#fff"/><rect x="7" y="4.5" width="6" height="11" rx="1" fill="var(--band-deep)"/><rect x="8" y="6" width="4" height="7" fill="#fff"/></svg>
        <span>021 555 0147</span>
      </li>
      <li>
        <svg viewBox="0 0 20 20"><circle cx="10" cy="10" r="10" fill="#fff"/><rect x="5" y="6.5" width="10" height="7" fill="var(--band-deep)"/><path d="M5 6.5l5 4 5-4" stroke="#fff" stroke-width="1" fill="none"/></svg>
        <span>d.marsh@brindloweng.com</span>
      </li>
      <li>
        <svg viewBox="0 0 20 20"><path d="M10 1a6.5 6.5 0 0 0-6.5 6.5C3.5 12 10 19 10 19s6.5-7 6.5-11.5A6.5 6.5 0 0 0 10 1z" fill="#fff"/><circle cx="10" cy="7.5" r="2.4" fill="var(--band-mid)"/></svg>
        <span>12th floor, 40 Harbour Line Road</span>
      </li>
    </ul>

    <div class="website">www.BrindlowEng.com</div>
  </div>
</body>
</html>
```